We have a small 501C Non-Profit, called Youngsters Unite. The non-profit was started by my son and his friends during the Gulf Oil Spill. We would like to update the website that currently sits on Domivault.com. I'm not sure how we transfer over the domain or get them to host it with your new design. I've attached a link of the old site that we developed. We are open to any ideas regarding hosting.

We would basically like a look that is youth (teen, college age) oriented that will drive teens and donors to the site. Our goal is to get onto Plixa Drives, get grants and make major donations with little to no administration expense. We will get sponsors to pay for the administration costs. So we will be looking for sponsors to support the overhead and 100% of donor money will go to causes important to teens.

http://www.youngstersunite.org

Target Market(s)

Teenagers and Individual Sponsors. Adults that want to help teens with an important cause.

Industry/Entity Type

Non-Profit

Requirements
Must have
• We are very open to ideas. It would be good to have a:

Home-with Mission Statement and Photos or Graphics
Donate-100% of Donations Go To Causes (with Coinvo Link)
Become A Sponsor-Insert Contact Information In This Section.
How It All Got Started -with info, articles, events, video, etc. from Gulf Oil Spill, Our Founder photo.
Contact-Change phone number to 555-804-2739. Keep e-mail and mailing the same.

You can use some existing photos from current site if you would like. All the Recent Event Photos, Founder Photo, 3 people holding check photo were all taken by me so there are no rights issues with those.

YU Mission Statement:

To demonstrate to the world that Youngsters Unite about the environment, each other and world peace through fund raising and other philanthropic efforts.
Nice to have
• Youngsters Unite Logo If Possible

Photo of 3 people, holding check, from existing home page in new History Section.

Kindpaw League Story and Logo in History Section

WRX Video in History Section

Helpio4
http://www.helpio4.net/stories/youth-launches-charity-to-fund-relief-for-wildlife-harmed-by-coastal-slick.html
Should not have
• Delete Blog Section
Delete Founder Section
Delete Recent Events
Delete How To Get Involved

```html
<!DOCTYPE html>
<html lang="en">
<head>
<meta charset="utf-8">
<title>Youngsters Unite</title>
<link href="https://fonts.googleapis.com/css2?family=Marcellus&family=Ubuntu:ital,wght@0,400;0,500;1,400&display=swap" rel="stylesheet">
<style>
  :root {
    --brand-blue: #4a6fa5;
    --brand-navy: #1f3a66;
    --ink: #111;
    --muted: #7a7a7a;
    --footer-ink: #555;
    --line: #d8d8d8;
    --paper: #fff;
  }
  * { box-sizing: border-box; margin: 0; padding: 0; }
  html, body { width: 1065px; height: 1200px; overflow: hidden; background: var(--paper); }
  body { position: relative; font-family: "Ubuntu", sans-serif; color: var(--ink); }

  .brand { position: absolute; left: 80px; top: 24px; display: flex; align-items: center; gap: 14px; }
  .brand-name { font-family: "Marcellus", serif; font-size: 56px; color: var(--ink); letter-spacing: 1px; }
  .brand-mark { width: 96px; height: 96px; border-radius: 50%; background: var(--brand-blue); border: 3px solid var(--ink); }

  .social { position: absolute; right: 68px; top: 38px; display: flex; gap: 6px; }
  .social a { display: flex; align-items: center; justify-content: center; width: 38px; height: 36px;
    border: 1px solid #c8c8c8; border-radius: 4px; background: linear-gradient(#fafafa, #e4e4e4);
    font-size: 9px; font-weight: 500; color: var(--brand-navy); text-decoration: none; }
  .phone { position: absolute; right: 68px; top: 81px; font-size: 21px; color: var(--muted); }

  .nav-band { position: absolute; left: 68px; width: 930px; top: 150px; height: 74px;
    border-top: 1px solid var(--line); box-shadow: 0 6px 6px -6px rgba(0,0,0,.35); }
  .main-nav { position: absolute; left: 68px; top: 164px; display: flex; }
  .main-nav a { display: block; height: 46px; line-height: 46px; padding: 0 14px; font-size: 19px; color: var(--ink); text-decoration: none; }
  .main-nav a.active { background: var(--brand-blue); color: #fff; border-radius: 3px; }
  .search { position: absolute; left: 765px; top: 170px; width: 228px; height: 36px; border: 1px solid #bbb; border-radius: 18px;
    box-shadow: inset 0 1px 3px rgba(0,0,0,.15); display: flex; align-items: center; padding: 0 10px 0 14px; }
  .search span { flex: 1; font-style: italic; color: var(--brand-blue); font-size: 16px; }

  .hero { position: absolute; left: 69px; top: 263px; width: 927px; height: 443px; border-radius: 8px; overflow: hidden;
    background:
      radial-gradient(ellipse 22% 55% at 50% 42%, rgba(240,240,236,.85), rgba(240,240,236,0) 100%),
      radial-gradient(ellipse 22% 50% at 80% 48%, rgba(150,175,215,.8), rgba(150,175,215,0) 100%),
      radial-gradient(ellipse 22% 50% at 22% 48%, rgba(170,172,140,.8), rgba(170,172,140,0) 100%),
      linear-gradient(180deg, transparent 60%, rgba(214,220,224,.95) 72%, #e2e6e8 100%),
      linear-gradient(180deg, #9a5b3c 0%, #6b4632 18%, #4a3428 45%, #3a2b24 100%);
    box-shadow: 0 10px 10px -6px rgba(0,0,0,.4); }

  .feature { position: absolute; top: 770px; }
  .feature h2 { font-size: 27px; font-weight: 500; color: var(--brand-blue); text-align: center; margin-bottom: 12px; }
  .feature p { font-style: italic; font-size: 16px; line-height: 24px; color: var(--muted); letter-spacing: .3px; }
  .feature .media { position: absolute; top: 125px; }
  .mission { left: 68px; width: 284px; }
  .mission .media { left: 2px; width: 277px; height: 157px;
    background:
      linear-gradient(180deg, rgba(230,210,70,.9) 0%, rgba(230,210,70,0) 14%),
      radial-gradient(ellipse 60% 45% at 50% 62%, rgba(245,245,245,.9), rgba(245,245,245,0) 100%),
      linear-gradient(180deg, #9a8a5a 0%, #7d7a6e 60%, #4d4a44 100%); }
  .kindpaw { left: 407px; width: 282px; }
  .kindpaw .media { left: 33px; width: 217px; height: 132px; border-radius: 26px 14px 40px 30px;
    background: radial-gradient(ellipse at 50% 45%, #2c4a7c, var(--brand-navy) 75%); }
  .video { left: 735px; width: 266px; }
  .video .media { left: 1px; width: 263px; height: 157px; border-right: 3px solid #4a4fb0;
    background:
      radial-gradient(ellipse 30% 55% at 42% 40%, rgba(200,170,150,.55), rgba(200,170,150,0) 100%),
      linear-gradient(90deg, #2a2a2e 0%, #3a3b44 55%, #4a5a7a 80%, #2a3050 100%); }
  .video .play { position: absolute; left: 91px; top: 46px; }

  .site-footer { position: absolute; left: 68px; width: 930px; top: 1108px; border-top: 1px solid var(--line); text-align: center; color: var(--footer-ink); font-size: 16px; }
  .site-footer nav { margin-top: 27px; }
  .site-footer a { color: var(--footer-ink); text-decoration: none; }
  .sep { margin: 0 9px; }
  .legal { margin-top: 6px; }
</style>
</head>
<body>
  <header>
    <div class="brand">
      <span class="brand-name">Youngsters Unite</span>
      <span class="brand-mark"></span>
    </div>
    <div class="social">
      <a href="#">Vidora</a><a href="#">Plixa</a><a href="#">Chirpo</a><a href="#">Feed</a>
    </div>
    <div class="phone">Ph: 555-804-2739</div>
  </header>

  <div class="nav-band"></div>
  <nav class="main-nav">
    <a class="active" href="#">Home</a>
    <a href="#">Donate</a>
    <a href="#">Become a Sponsor</a>
    <a href="#">How it all got started</a>
    <a href="#">Contact us</a>
  </nav>
  <div class="search">
    <span>Search here...</span>
    <svg width="26" height="26" viewBox="0 0 26 26" aria-hidden="true">
      <circle cx="10" cy="10" r="7.5" fill="none" stroke="#4a6fa5" stroke-width="3"/>
      <line x1="15.5" y1="15.5" x2="23" y2="23" stroke="#4a6fa5" stroke-width="4" stroke-linecap="round"/>
    </svg>
  </div>

  <div class="hero" role="img" aria-label="Photo of three people holding a large donation check at an outdoor café"></div>

  <section class="feature mission">
    <h2>Our Mission</h2>
    <p>&nbsp;Support each other, the environment and the poor, through fund raising and other philanthropic efforts.</p>
    <div class="media" role="img" aria-label="Group photo of teenage volunteers at a fundraising stand"></div>
  </section>

  <section class="feature kindpaw">
    <h2>The Kindpaw League</h2>
    <p>&nbsp;&nbsp;Young people across the country are determined to help animals in the Gulf.</p>
    <div class="media" role="img" aria-label="Illustration of animal silhouettes forming a map of the country"></div>
  </section>

  <section class="feature video">
    <h2>WRX Video</h2>
    <p>Teen raises thousands for oil soaked wildlife.</p>
    <div class="media" role="img" aria-label="News broadcast video still about the oil spill">
      <svg class="play" width="86" height="86" viewBox="0 0 86 86" aria-hidden="true">
        <circle cx="43" cy="43" r="40" fill="rgba(255,255,255,.12)" stroke="#bbb" stroke-width="4"/>
        <polygon points="33,26 62,43 33,60" fill="#bbb"/>
      </svg>
    </div>
  </section>

  <footer class="site-footer">
    <nav>
      <a href="#">Home</a><span class="sep">|</span><a href="#">Donate</a><span class="sep">|</span><a href="#">Become a Sponsor</a><span class="sep">|</span><a href="#">How it all got started</a><span class="sep">|</span><a href="#">Contact us</a>
    </nav>
    <div class="legal">© 2012 Youngsters Unite<span class="sep">|</span><a href="#">Terms of use</a><span class="sep">|</span><a href="#">Privacy policy</a></div>
  </footer>
</body>
</html>
```